Advertisement insert for magazine

Create a 5 X 4.75 advertisement for a magazine. Design must catch the eye of the reader and properly represent our brand. This will be in LANTERN magazine a local affluent magazine.

The goal of this advertisement is to represent a progressive firm with an amazing portfolio.

Target Market(s)

local businesses and business leaders of Florida.

Industry/Entity Type

Architecture

Font styles to use
Other font styles liked:
• Calibri, Calibri light

Requirements
Must have
• Modern Progressive Design. Our logo, our address and telephone number and our project images we have attached.
Should not have
• I have attached the ad from last year, we DO NOT want to replicate this ad, however this should give you an idea of the size and overall goal of the advertisement.
• (SEE LANTERN MAGAZINE KTW PDF)

```html
<!DOCTYPE html>
<html lang="en">
<head>
<meta charset="utf-8">
<title>HarborLane Magazine Ad Options</title>
<link href="https://fonts.googleapis.com/css2?family=Open+Sans:wght@400;600&family=EB+Garamond:wght@400&display=swap" rel="stylesheet">
<style>
  :root {
    --board-bg: #ffffff;
    --brand-blue: #1a6fc0;
    --brand-blue-deep: #1560b0;
    --panel-grey: #d2d2d2;
    --footer-grey: #e6e6e6;
    --footer-grey-dark: #a3a3a3;
    --label-band: #231f20;
    --outline: #8d8d8d;
    --ink-dark: #2a2a2a;
    --white: #ffffff;
  }
  * { box-sizing: border-box; margin: 0; padding: 0; }
  html, body { width: 1200px; height: 616px; overflow: hidden; background: var(--board-bg); }
  body { position: relative; font-family: "Open Sans", Calibri, sans-serif; }

  .ad { position: absolute; top: 55px; width: 481px; height: 457px; overflow: hidden; border: 1px solid #5b7fc4; }
  .ad--option-one { left: 52px; background: var(--white); }
  .ad--option-two { left: 670px; background: var(--brand-blue); }

  .photo { position: absolute; border: 2px solid var(--white); outline: 1px solid var(--outline); }

  .tone-dusk-store { background: linear-gradient(180deg, #3f63ad 0%, #8fa8d6 45%, #4b4a48 70%, #2b2b2b 100%); }
  .tone-lobby-night { background: linear-gradient(180deg, #7c8fc2 0%, #c9b9c9 35%, #3c5a3b 65%, #2d2f35 100%); }
  .tone-pink-sky { background: linear-gradient(180deg, #a98cc4 0%, #e8b59a 40%, #a77a55 65%, #4a3a33 100%); }
  .tone-lounge { background: linear-gradient(160deg, #e3e0d6 0%, #b9c8cf 40%, #3e5f93 70%, #c8a77a 100%); }
  .tone-bar { background: linear-gradient(180deg, #6f8f93 0%, #4f6f6d 40%, #c48a55 70%, #e4ddd2 100%); }
  .tone-showroom { background: linear-gradient(180deg, #c9a3a3 0%, #e4c0a5 40%, #7a8a90 70%, #3f4346 100%); }
  .tone-stair { background: linear-gradient(135deg, #f2f0ea 0%, #d8d4cc 50%, #3a3a3a 100%); }
  .tone-condo { background: linear-gradient(180deg, #8eb7de 0%, #cfe0ee 40%, #e9e9e6 60%, #d5467a 100%); }
  .tone-office { background: linear-gradient(180deg, #d9d3c6 0%, #bfb6a6 40%, #8e8a84 70%, #d2cbc0 100%); }
  .tone-hall { background: linear-gradient(180deg, #7a4a2a 0%, #a97a50 40%, #c7a489 70%, #8a3a2a 100%); }

  .panel-curve { position: absolute; left: 0; top: 0; }
  .band-blue { position: absolute; left: 0; top: 297px; width: 481px; height: 120px; background: var(--brand-blue); }

  .brand { position: absolute; display: flex; flex-direction: column; align-items: center; }
  .brand__row { display: flex; align-items: center; gap: 6px; }
  .brand__dot { border-radius: 50%; background: var(--brand-blue); }
  .brand__name { font-family: "Open Sans", Calibri, sans-serif; font-weight: 600; color: var(--ink-dark); letter-spacing: 0.5px; }
  .brand__tagline { font-size: 5.5px; letter-spacing: 1px; color: var(--ink-dark); margin-top: 6px; }
  .ad--option-one .brand { left: 278px; top: 37px; width: 170px; }
  .ad--option-one .brand__dot { width: 40px; height: 40px; }
  .ad--option-one .brand__name { font-size: 17px; }

  .logo-card { position: absolute; left: 166px; top: 369px; width: 150px; height: 49px; background: var(--white); }
  .logo-card .brand { left: 0; top: 6px; width: 150px; }
  .logo-card .brand__dot { width: 28px; height: 28px; }
  .logo-card .brand__name { font-size: 13px; }
  .logo-card .brand__tagline { font-size: 4.5px; margin-top: 3px; }

  .footer { position: absolute; left: 0; bottom: 0; width: 100%; height: 40px; display: flex; align-items: center; justify-content: center; }
  .footer__item { font-size: 10px; padding: 0 14px; }
  .footer__item--phone { font-size: 13px; font-weight: 600; }
  .footer__divider { width: 1px; height: 26px; }
  .ad--option-one .footer { background: var(--footer-grey); color: var(--brand-blue); }
  .ad--option-one .footer__divider { background: var(--brand-blue); }
  .ad--option-two .footer { height: 55px; background: var(--footer-grey-dark); color: var(--white); border-top: 3px solid var(--white); padding-top: 8px; }
  .ad--option-two .footer__divider { background: var(--white); }

  .guide { position: absolute; border-color: rgba(255,255,255,0.55); border-style: dotted; border-width: 0; }
  .guide--h { border-top-width: 1px; height: 0; }
  .guide--v { border-left-width: 1px; width: 0; }

  .label-band { position: absolute; left: 0; top: 562px; width: 1200px; height: 48px; background: var(--label-band); }
  .label { position: absolute; top: 14px; font-family: "EB Garamond", Georgia, serif; font-size: 17px; color: var(--white); letter-spacing: 0.5px; transform: translateX(-50%); white-space: nowrap; }
</style>
</head>
<body>

<section class="ad ad--option-one">
  <svg class="panel-curve" width="481" height="297" viewBox="0 0 481 297" aria-hidden="true">
    <path d="M22,0 H252 C232,60 230,200 250,297 H24 C42,200 40,60 22,0 Z" fill="#d9d9d9"/>
    <path d="M60,0 H214 C200,60 198,200 212,297 H62 C74,200 72,60 60,0 Z" fill="#c8c8c8"/>
  </svg>

  <div class="photo tone-dusk-store" style="left:56px;top:15px;width:162px;height:85px" role="img" aria-label="Hardware store exterior at dusk"></div>
  <div class="photo tone-lobby-night" style="left:56px;top:109px;width:162px;height:84px" role="img" aria-label="Residential tower entrance canopy at night"></div>
  <div class="photo tone-pink-sky" style="left:56px;top:199px;width:162px;height:86px" role="img" aria-label="Historic arcaded building under pink sky"></div>

  <div class="brand">
    <div class="brand__row"><span class="brand__dot"></span><span class="brand__name">HARBORLANE</span></div>
    <div class="brand__tagline">ARCHITECTURE &nbsp;•&nbsp; INTERIOR DESIGN</div>
  </div>

  <div class="photo tone-lounge" style="left:262px;top:112px;width:96px;height:96px" role="img" aria-label="Bright lounge with blue sofa"></div>
  <div class="photo tone-bar" style="left:367px;top:112px;width:95px;height:96px" role="img" aria-label="Restaurant bar with pendant lights"></div>
  <div class="photo tone-showroom" style="left:262px;top:215px;width:200px;height:66px" role="img" aria-label="Car showroom exterior with palm trees"></div>

  <div class="band-blue"></div>
  <div class="photo tone-stair" style="left:10px;top:306px;width:107px;height:103px" role="img" aria-label="White lobby with glass staircase"></div>
  <div class="photo tone-condo" style="left:127px;top:306px;width:107px;height:103px" role="img" aria-label="White condominium with flowering bougainvillea"></div>
  <div class="photo tone-office" style="left:245px;top:306px;width:107px;height:103px" role="img" aria-label="Open office lounge with banquette seating"></div>
  <div class="photo tone-hall" style="left:362px;top:306px;width:108px;height:103px" role="img" aria-label="Wood-beamed hall with lanterns"></div>

  <footer class="footer">
    <span class="footer__item">48 Coral Avenue, West Palm Beach, Florida</span>
    <span class="footer__divider"></span>
    <span class="footer__item footer__item--phone">(561) 555-0192</span>
    <span class="footer__divider"></span>
    <span class="footer__item">HarborLane.com</span>
  </footer>
</section>

<section class="ad ad--option-two">
  <div class="guide guide--h" style="left:10px;top:37px;width:140px"></div>
  <div class="guide guide--h" style="left:330px;top:37px;width:140px"></div>
  <div class="guide guide--h" style="left:10px;top:315px;width:140px"></div>
  <div class="guide guide--h" style="left:330px;top:315px;width:140px"></div>
  <div class="guide guide--v" style="left:148px;top:7px;height:340px"></div>
  <div class="guide guide--v" style="left:329px;top:7px;height:340px"></div>

  <div class="photo tone-bar" style="left:30px;top:42px;width:119px;height:86px" role="img" aria-label="Restaurant bar with pendant lights"></div>
  <div class="photo tone-condo" style="left:30px;top:134px;width:119px;height:84px" role="img" aria-label="White condominium with flowering bougainvillea"></div>
  <div class="photo tone-stair" style="left:30px;top:223px;width:119px;height:86px" role="img" aria-label="White lobby with glass staircase"></div>

  <div class="photo tone-showroom" style="left:157px;top:13px;width:168px;height:86px" role="img" aria-label="Car showroom exterior with palm trees"></div>
  <div class="photo tone-dusk-store" style="left:157px;top:106px;width:168px;height:86px" role="img" aria-label="Hardware store exterior at dusk"></div>
  <div class="photo tone-lobby-night" style="left:157px;top:198px;width:168px;height:87px" role="img" aria-label="Residential tower entrance canopy at night"></div>
  <div class="photo tone-pink-sky" style="left:157px;top:291px;width:168px;height:87px" role="img" aria-label="Historic arcaded building under pink sky"></div>

  <div class="photo tone-hall" style="left:332px;top:42px;width:119px;height:86px" role="img" aria-label="Wood-beamed hall with lanterns"></div>
  <div class="photo tone-office" style="left:332px;top:134px;width:119px;height:84px" role="img" aria-label="Open office lounge with banquette seating"></div>
  <div class="photo tone-lounge" style="left:332px;top:223px;width:119px;height:86px" role="img" aria-label="Bright lounge with blue sofa"></div>

  <footer class="footer">
    <span class="footer__item">48 Coral Avenue, West Palm Beach, Florida</span>
    <span class="footer__divider"></span>
    <span class="footer__item footer__item--phone">(561) 555-0192</span>
    <span class="footer__divider"></span>
    <span class="footer__item">HarborLane.com</span>
  </footer>

  <div class="logo-card">
    <div class="brand">
      <div class="brand__row"><span class="brand__dot"></span><span class="brand__name">HARBORLANE</span></div>
      <div class="brand__tagline">ARCHITECTURE &nbsp;•&nbsp; INTERIOR DESIGN</div>
    </div>
  </div>
</section>

<div class="label-band">
  <span class="label" style="left:294px">MAGAZINE AD OPTION 1</span>
  <span class="label" style="left:904px">MAGAZINE AD OPTION 2</span>
</div>

</body>
</html>
```